Harbourline Blinds & Shutters

It Needs to look classy as my target is the upper end of the blind market
I need a Logo design on front and description on back of what i do:
- Roller Blinds
- Vertical Blinds
- Venetian Blinds
- Plantation Shutters
- Aluminum External Shutters
and contact details
Gavin
0418527306
and
Terry
0421690358
Updates
Hi Guys,
Sorry for the no feedback but i was waiting on my logo design. But its done now i have uploaded it. so if you could take a look and send through some designs
Reason: my logo was just finished an i just uploaded it today really dont understand why my deadline has been rached foe my bizcards as it states no deadline. But please extend
Target Market(s)
People that live on the coast and are looking for classy good quality blinds and shutters
Font styles to use
Other font styles liked:
- Copperplate Gothic,open to suggestion
Look and feel
Each slider illustrates characteristics of the customer's brand and the style your logo design should communicate.

```html
<!DOCTYPE html>
<html lang="en">
<head>
<meta charset="utf-8">
<title>Harbourline Blinds &amp; Shutters – Business Card</title>
<link rel="stylesheet" href="https://fonts.googleapis.com/css2?family=Montserrat:wght@400;600;700&display=swap">
<style>
  :root {
    --page-bg: #e9e7e3;
    --card-black: #111112;
    --card-black-soft: #1d1d1f;
    --silver: #d9d9dc;
    --silver-dim: #9a9a9e;
    --gold: #d9a837;
    --gold-deep: #a8781c;
    --divider: #4a4a4e;
  }
  * { box-sizing: border-box; margin: 0; padding: 0; }
  html, body { width: 1200px; height: 855px; overflow: hidden; }
  body {
    background: var(--page-bg);
    font-family: "Montserrat", Arial, sans-serif;
    display: flex;
    align-items: center;
    justify-content: center;
    gap: 40px;
  }
  .card {
    width: 560px;
    height: 320px;
    border-radius: 22px;
    background: linear-gradient(135deg, var(--card-black-soft) 0%, var(--card-black) 55%, #0a0a0b 100%);
    box-shadow: 0 14px 30px rgba(0,0,0,.35);
    position: relative;
    overflow: hidden;
    color: var(--silver);
  }
  .brand-disc {
    border-radius: 50%;
    background: radial-gradient(circle at 40% 35%, var(--gold) 0%, var(--gold-deep) 100%);
    border: 6px solid #8d8d91;
    flex: none;
  }

  /* Front */
  .card--front {
    display: flex;
    align-items: center;
    justify-content: center;
    gap: 22px;
  }
  .card--front .brand-disc { width: 96px; height: 96px; }
  .front-name {
    font-weight: 600;
    font-size: 24px;
    letter-spacing: 2px;
    text-transform: uppercase;
    color: var(--silver);
    line-height: 1.3;
  }

  /* Back */
  .card--back { padding: 26px 30px; }
  .back-heading {
    position: absolute;
    top: 26px;
    right: 30px;
    font-weight: 700;
    font-size: 21px;
    letter-spacing: 1.5px;
    text-transform: uppercase;
    color: var(--silver);
  }
  .card--back .brand-disc {
    position: absolute;
    left: 40px;
    top: 76px;
    width: 120px;
    height: 120px;
  }
  .services {
    position: absolute;
    left: 205px;
    top: 86px;
  }
  .services-title {
    font-weight: 700;
    font-size: 14px;
    letter-spacing: 1px;
    color: var(--gold);
    text-transform: uppercase;
    margin-bottom: 4px;
  }
  .services-list { list-style: none; font-size: 14px; line-height: 1.55; color: #f0f0f0; }
  .services-list li::before { content: "•"; margin-right: 6px; }
  .contacts {
    position: absolute;
    left: 30px;
    bottom: 26px;
    display: flex;
    align-items: stretch;
  }
  .contact { padding: 0 18px; }
  .contact:first-child { padding-left: 0; }
  .contact + .contact { border-left: 1px solid var(--divider); }
  .contact-name { font-weight: 700; font-size: 17px; color: var(--gold); }
  .contact-phone { font-size: 18px; color: #f2f2f2; letter-spacing: .5px; }
</style>
</head>
<body>
  <section class="card card--front" aria-label="Card front">
    <div class="brand-disc" aria-hidden="true"></div>
    <h1 class="front-name">Harbourline<br>Blinds &amp; Shutters</h1>
  </section>

  <section class="card card--back" aria-label="Card back">
    <h2 class="back-heading">Harbourline Blinds &amp; Shutters</h2>
    <div class="brand-disc" aria-hidden="true"></div>
    <div class="services">
      <p class="services-title">Services</p>
      <ul class="services-list">
        <li>Roller Blinds</li>
        <li>Vertical Blinds</li>
        <li>Venetian Blinds</li>
        <li>Plantation Shutters</li>
        <li>Aluminum External Shutters</li>
      </ul>
    </div>
    <div class="contacts">
      <div class="contact">
        <p class="contact-name">Gavin</p>
        <p class="contact-phone">0418527306</p>
      </div>
      <div class="contact">
        <p class="contact-name">Terry</p>
        <p class="contact-phone">0421690358</p>
      </div>
    </div>
  </section>
</body>
</html>
```